brightwave - Property Management DL Card

I am after a savvy designer to cut through junk mail! so many real estate agents use flyers to promote themselves and their business and usually sales. We are a property management firm (residential) and we want to represent landlords that have existing investment properties and need a quality agent to represent them. Can you help?
DL size, will be printed and delivered to mailboxes. For a look at our website go to www.brightwavehq.com.au. Keep it simple and clutter free.
it is to be double sided - with one side to be simple and clear - just our website, logo and telephone number on the back.
attached is our logo and our telephone number is 1300 42 18 96
the above are 2 essential elements to be included + our email address: admin@brightwavehq.com.au
also attached are our transparent price list

Target Market(s)
property investors,
people that manage properties themselves
Industry/Entity Type
Property Management
Other font styles liked:
- arial
Look and feel

```html
<!DOCTYPE html>
<html lang="en">
<head>
<meta charset="utf-8">
<title>brightwave – Property Management DL Card</title>
<link href="https://fonts.googleapis.com/css2?family=Arimo:wght@400;700&family=Raleway:wght@400&display=swap" rel="stylesheet">
<style>
  :root {
    --page: #e9e4dd;
    --card: #ffffff;
    --ink: #111111;
    --band: #8f9093;
    --band-light: #a9aaac;
    --edge: #b5b6b8;
    --logo: #2b2b2b;
    --photo-warm-a: #e9dcc4;
    --photo-warm-b: #8a7458;
    --photo-cool-a: #f1f1ef;
    --photo-cool-b: #7d7b78;
  }
  * { box-sizing: border-box; margin: 0; padding: 0; }
  html, body { width: 1200px; height: 900px; overflow: hidden; }
  body {
    position: relative;
    background: var(--page);
    font-family: "Arimo", Arial, sans-serif;
    color: var(--ink);
  }
  .card {
    position: absolute;
    width: 945px;
    height: 433px;
    background: var(--card);
    overflow: hidden;
    box-shadow: 0 2px 10px rgba(0,0,0,0.18);
  }
  .card--front { left: 23px; top: 16px; }
  .card--back  { left: 239px; top: 457px; }
  .card__art { position: absolute; left: 0; top: 0; width: 945px; height: 433px; }

  .brand {
    position: absolute;
    font-family: "Raleway", Arial, sans-serif;
    font-weight: 400;
    font-size: 52px;
    letter-spacing: 1px;
    color: var(--logo);
    line-height: 1;
  }
  .card--front .brand { left: 150px; top: 42px; }
  .card--back .brand  { left: 565px; top: 32px; }

  .headline {
    position: absolute;
    font-weight: 700;
    font-size: 23px;
    white-space: nowrap;
  }
  .card--front .headline { left: 21px; top: 156px; }
  .card--back .headline  { left: 433px; top: 200px; width: 530px; text-align: center; }

  .benefits {
    position: absolute;
    left: 172px;
    top: 237px;
    list-style: none;
    font-weight: 700;
    font-size: 15px;
    line-height: 27px;
  }
  .benefits li::before {
    content: "";
    display: inline-block;
    width: 12px; height: 12px;
    border-radius: 50%;
    background: var(--ink);
    margin-right: 5px;
    vertical-align: -1px;
  }

  .band-text {
    position: absolute;
    top: 398px;
    color: #fff;
    font-weight: 700;
    font-size: 19px;
    white-space: nowrap;
  }
  .band-text--phone { left: 2px; }
  .band-text--email { left: 325px; font-weight: 400; letter-spacing: 0.3px; }

  .call {
    position: absolute;
    left: 420px; top: 335px;
    width: 560px;
    text-align: center;
    font-weight: 700;
    font-size: 27px;
    white-space: nowrap;
  }
  .contact {
    position: absolute;
    top: 400px;
    display: flex;
    align-items: center;
    gap: 6px;
    color: #fff;
    font-size: 17px;
    white-space: nowrap;
  }
  .contact--email { left: 340px; }
  .contact--web { left: 605px; }
  .contact svg { width: 24px; height: 24px; }
</style>
</head>
<body>

<section class="card card--front">
  <svg class="card__art" viewBox="0 0 945 433" aria-hidden="false">
    <defs>
      <linearGradient id="warmRoom" x1="0" y1="0" x2="1" y2="1">
        <stop offset="0" stop-color="var(--photo-warm-a)"/>
        <stop offset="1" stop-color="var(--photo-warm-b)"/>
      </linearGradient>
    </defs>
    <rect x="0" y="387" width="650" height="46" fill="var(--band)"/>
    <polygon points="650,0 945,0 945,433 626,433 482,118" fill="var(--edge)"/>
    <polygon role="img" aria-label="Photo of a bright open-plan living room with sofa, dining area and kitchen"
      points="660,0 945,0 945,433 636,433 493,118" fill="url(#warmRoom)"/>
  </svg>
  <div class="brand">brightwave</div>
  <h1 class="headline">We Specialise In Property Management</h1>
  <ul class="benefits">
    <li>No postage and admin fees</li>
    <li>No hidden extras</li>
    <li>Excellent communication</li>
    <li>Technology focussed</li>
  </ul>
  <p class="band-text band-text--phone">Cal Us Today: 1300 42 18 96</p>
  <p class="band-text band-text--email">E-mail: admin@brightwavehq.com.au</p>
</section>

<section class="card card--back">
  <svg class="card__art" viewBox="0 0 945 433">
    <defs>
      <linearGradient id="coolRoom" x1="0" y1="0" x2="1" y2="1">
        <stop offset="0" stop-color="var(--photo-cool-a)"/>
        <stop offset="1" stop-color="var(--photo-cool-b)"/>
      </linearGradient>
    </defs>
    <rect x="300" y="387" width="645" height="46" fill="var(--band-light)"/>
    <polygon points="0,0 340,0 502,164 468,433 0,433" fill="var(--edge)"/>
    <polygon role="img" aria-label="Photo of a white living room with sofas, rug, coffee table and television"
      points="0,0 328,0 490,164 456,433 0,433" fill="url(#coolRoom)"/>
  </svg>
  <div class="brand">brightwave</div>
  <h2 class="headline">Competitive Fees For All Budgets</h2>
  <p class="call">Cal Us Today: 1300 42 18 96</p>
  <p class="contact contact--email">
    <svg viewBox="0 0 24 24" aria-hidden="true"><circle cx="12" cy="12" r="11" fill="none" stroke="#222" stroke-width="1.6"/><rect x="6" y="8" width="12" height="8" fill="none" stroke="#222" stroke-width="1.4"/><path d="M6 8l6 5 6-5" fill="none" stroke="#222" stroke-width="1.4"/></svg>
    admin@brightwavehq.com.au
  </p>
  <p class="contact contact--web">
    <svg viewBox="0 0 24 24" aria-hidden="true"><circle cx="12" cy="12" r="11" fill="#222"/><ellipse cx="12" cy="12" rx="5" ry="11" fill="none" stroke="#fff" stroke-width="1"/><path d="M1 12h22M3 6h18M3 18h18" stroke="#fff" stroke-width="1"/></svg>
    www.brightwavehq.com.au
  </p>
</section>

</body>
</html>
```